New custom software business needs a Wordpress site

We need a Wordpress site for a new company based out of Chicago called 'Brackwell Consulting'. Using a mix of on and off-shore resources we build custom software solutions, mainly focusing on small to medium sized companies. We help our customers "aspire" to do great things.
We have a basic site up here: https://brackwellhq.com/. We worked on the content for it but not the branding. For now, this houses all the pages (except for a Contact Us page we'll be adding soon) for the foreseeable future.
We also have a new logo (attached) that we'd like to base the styling/colors on.
Target Market(s)
Small to medium sized companies that require tech resources
Industry/Entity Type
Software
Nice to have
- Teamwork, tech, professional but not elitist

```html
<!DOCTYPE html>
<html lang="en">
<head>
<meta charset="utf-8">
<title>Brackwell Consulting</title>
<link rel="stylesheet" href="https://fonts.googleapis.com/css2?family=Orbitron:wght@400;500&family=Exo+2:wght@400;500;600&family=Roboto:ital,wght@0,400;0,500;1,400&family=Overpass:wght@400&display=swap">
<style>
:root{
  --navy:#0a4db0;
  --navy-deep:#083c8c;
  --sky:#6ba6e3;
  --band:#3a86d6;
  --pale:#eef3fa;
  --ink:#2f3441;
  --muted:#545b68;
  --white:#ffffff;
  --line:#c9d3e0;
  --grey-mark:#8e939b;
}
*{margin:0;padding:0;box-sizing:border-box}
html,body{width:1200px;height:4104px;overflow:hidden}
body{position:relative;background:var(--white);font-family:"Roboto",Arial,sans-serif;color:var(--ink)}
.abs{position:absolute}
.display{font-family:"Orbitron",sans-serif;font-weight:400;letter-spacing:2px}
.sub{font-family:"Exo 2",sans-serif}

/* hero */
.hero-photo{left:0;top:0;width:1200px;height:717px;clip-path:polygon(0 0,100% 0,100% 630px,0 717px);
  background:linear-gradient(120deg,#0d2a6b 0%,#173f95 30%,#2c5fbb 55%,#4a7fd0 75%,#1e4aa5 100%)}
.brand{left:151px;top:22px;display:flex;align-items:center;gap:12px;color:var(--white)}
.brand-square{width:48px;height:48px;background:var(--sky)}
.brand-name{font-family:"Orbitron",sans-serif;font-size:26px;letter-spacing:2px;line-height:1}
.brand-tag{display:block;font-size:10px;letter-spacing:4px;color:#a9c9f0;margin-top:4px;text-align:center}
.nav{top:38px;left:551px;display:flex;gap:0;font-family:"Exo 2",sans-serif;font-size:13px;color:var(--white);letter-spacing:1px}
.nav a{color:inherit;text-decoration:none;position:absolute;white-space:nowrap}
.nav .active::after{content:"";position:absolute;left:0;right:0;bottom:-8px;height:2px;background:var(--white)}
.hero-mark{left:600px;top:300px;width:100px;height:100px;background:var(--sky)}
.hero-title{left:746px;top:282px;color:var(--white);font-size:42px;line-height:58px;letter-spacing:3px}
.hero-text{left:748px;top:404px;width:320px;color:var(--white);font-family:"Overpass",sans-serif;font-size:18px;line-height:23px;letter-spacing:.5px}

/* services */
.services-bg{left:0;top:630px;width:1200px;height:674px;background:var(--pale);clip-path:polygon(0 87px,100% 0,100% 100%,0 100%)}
.section-title{left:0;width:1200px;text-align:center;font-size:38px;color:var(--navy)}
.section-title .light{color:var(--sky)}
.service{width:300px;text-align:center;top:889px}
.service svg{display:block;margin:0 auto}
.service h3{font-family:"Exo 2",sans-serif;font-weight:500;font-size:20px;line-height:25px;color:var(--ink);margin-top:36px}
.service p{font-size:13px;line-height:19px;color:var(--muted);margin:14px auto 0;width:240px}
.divider{width:1px;height:196px;top:897px;background:var(--line)}
.btn{display:flex;align-items:center;justify-content:center;background:var(--navy);color:var(--white);font-family:"Orbitron",sans-serif;font-size:14px;letter-spacing:1.5px;text-decoration:none}

/* about */
.about-photo{left:96px;top:1435px;width:403px;height:403px;border-radius:50%;
  background:radial-gradient(circle at 60% 40%,#e8e3dc,#b9a996 60%,#6f5c4a)}
.about-title{left:561px;top:1440px;font-size:38px;color:var(--navy)}
.about-text{left:561px;top:1500px;width:480px;font-size:14px;line-height:20.6px;color:var(--muted)}
.about-text p+p{margin-top:20px}

/* testimonials */
.testi-bg{left:0;top:1889px;width:1200px;height:709px;clip-path:polygon(0 111px,100% 0,100% 598px,0 709px);
  background:linear-gradient(110deg,#2f7bcf,#4a92dc 50%,#3581d3)}
.testi-title{top:2040px;color:var(--white)}
.testi-card{top:2171px;width:295px;height:229px;border:2px solid rgba(255,255,255,.85);text-align:center;color:var(--white);padding:60px 14px 0}
.testi-card blockquote{font-style:italic;font-size:14px;line-height:19.5px}
.testi-card .name{font-family:"Exo 2",sans-serif;font-weight:600;font-size:16px;margin-top:14px}
.testi-card .role{font-family:"Exo 2",sans-serif;font-size:14px;margin-top:1px}
.avatar{top:2129px;width:72px;height:72px;border-radius:50%;border:3px solid var(--white)}

/* blog */
.blog-card{top:2777px;height:381px;background:var(--pale)}
.blog-card .thumb{height:177px}
.blog-card h3{font-family:"Exo 2",sans-serif;font-weight:500;font-size:19px;line-height:23px;color:var(--navy);margin:32px 28px 0}
.blog-card p{font-size:11.5px;line-height:17px;color:var(--ink);margin:12px 28px 0}
.blog-card svg{position:absolute;left:28px;bottom:26px}

/* partners */
.partners-bg{left:0;top:3273px;width:1200px;height:425px;background:var(--pale)}
.partners-title{top:3350px;font-size:28px;color:#3a3f4a;letter-spacing:3px}
.partner{top:3430px;background:var(--grey-mark);opacity:.75}

/* footer */
.footer-bg{left:0;top:3610px;width:1200px;height:494px;background:linear-gradient(180deg,var(--navy),var(--navy-deep));clip-path:polygon(0 88px,100% 0,100% 100%,0 100%)}
.footer-brand{left:156px;top:3790px;width:227px;text-align:center;color:var(--white)}
.footer-brand .brand-square{width:110px;height:110px;margin:0 auto 20px;background:var(--sky)}
.footer-brand .name{font-family:"Orbitron",sans-serif;font-size:30px;letter-spacing:2px}
.footer-brand .tag{font-family:"Orbitron",sans-serif;font-size:13px;letter-spacing:5px;color:#8fb8ee;border-top:1px solid #8fb8ee;margin-top:4px;padding-top:3px}
.footer-col{top:3783px;color:var(--white)}
.footer-col h4{font-family:"Orbitron",sans-serif;font-weight:400;font-size:22px;letter-spacing:2px;margin-bottom:16px}
.footer-col li{list-style:none;font-size:12px;line-height:25px}
.social{left:908px;top:3897px;display:flex;gap:14px}
.social span{width:20px;height:20px;border-radius:50%;background:var(--white)}
.footer-rule{left:156px;top:4025px;width:936px;height:1px;background:rgba(255,255,255,.35)}
.copyright{left:0;top:4055px;width:1200px;text-align:center;color:var(--white);font-size:12px}
</style>
</head>
<body>

<!-- hero -->
<div class="abs hero-photo" role="img" aria-label="Photo looking up at a glass skyscraper against a blue cloudy sky"></div>
<div class="abs brand">
  <span class="brand-square"></span>
  <span><span class="brand-name">BRACKWELL</span><span class="brand-tag">CONSULTING</span></span>
</div>
<nav class="abs nav">
  <a class="active" style="left:0">HOME</a>
  <a style="left:79px">SERVICES</a>
  <a style="left:184px">WHY BRACKWELL?</a>
  <a style="left:338px">BRACKWELL LEADERSHIP</a>
</nav>
<div class="abs hero-mark"></div>
<h1 class="abs display hero-title">BRACKWELL<br>CONSULTING</h1>
<p class="abs hero-text">Software consulting company specializing in serving small to medium size businesses.</p>

<!-- services -->
<div class="abs services-bg"></div>
<h2 class="abs display section-title" style="top:774px"><span class="light">OUR</span> SERVICES</h2>

<div class="abs service" style="left:108px">
  <svg width="64" height="64" viewBox="0 0 64 64" fill="none" stroke="#0a4db0" stroke-width="2"><path d="M8 8h20v6a5 5 0 0 0 10 0V8h18v20h-6a5 5 0 0 0 0 10h6v18H36v-6a5 5 0 0 0-10 0v6H8V36h6a5 5 0 0 0 0-10H8z"/></svg>
  <h3>Custom Solution<br>Delivery</h3>
  <p>Brackwell offers a range of services focused on helping businesses and organizations deliver software</p>
</div>
<div class="abs divider" style="left:435px"></div>
<div class="abs service" style="left:450px">
  <svg width="70" height="64" viewBox="0 0 70 64" fill="none" stroke="#0a4db0" stroke-width="2"><circle cx="35" cy="12" r="8"/><circle cx="17" cy="24" r="7"/><circle cx="53" cy="24" r="7"/><path d="M4 60V46a10 10 0 0 1 20 0v14M46 60V46a10 10 0 0 1 20 0v14M22 60V38a13 13 0 0 1 26 0v22"/></svg>
  <h3>Staff<br>Augmentation</h3>
  <p>Let Brackwell help you supplement your existing software development teams with additional resources</p>
</div>
<div class="abs divider" style="left:775px"></div>
<div class="abs service" style="left:784px">
  <svg width="64" height="64" viewBox="0 0 64 64" fill="none" stroke="#0a4db0" stroke-width="2"><rect x="6" y="6" width="52" height="38" rx="2"/><path d="M26 44l-3 12h18l-3-12M18 58h28M28 19l-6 6 6 6M36 19l6 6-6 6M34 17l-4 16"/></svg>
  <h3>Custom Software<br>Solutions</h3>
  <p>Brackwell offers a range of services focused on helping businesses and organizations deliver software</p>
</div>
<a class="abs btn" style="left:480px;top:1151px;width:237px;height:49px">VIEW OUR SERVICES</a>

<!-- about -->
<div class="abs about-photo" role="img" aria-label="Photo of a woman working at a desk in a bright office"></div>
<h2 class="abs display about-title">ABOUT US</h2>
<div class="abs about-text">
  <p>Welcome to Brackwell, a software consulting company specializing in serving small to medium size businesses. We understand the unique challenges and opportunities that these companies face, and we are dedicated to helping them succeed through innovative technology solutions.</p>
  <p>Our team of experienced professionals has a diverse range of skills and expertise, making us well-equipped to handle any project, big or small. We specialize in custom software development, working closely with our clients to understand their specific needs and build solutions that meet their requirements.</p>
</div>
<a class="abs btn" style="left:566px;top:1757px;width:131px;height:43px;font-size:12px">READ MORE</a>

<!-- testimonials -->
<div class="abs testi-bg" role="img" aria-label="Blue-tinted photo of a team collaborating around a table"></div>
<h2 class="abs display section-title testi-title">TESTIMONIALS</h2>

<div class="abs testi-card" style="left:135px">
  <blockquote>“Lorem ipsum dolor sit amet, ctetulor ehsed do eiusmod tempor incididun ut et dolore ma aliquauilorlore mes ipsusus pendisseiusmod tempor incididunt ut labore et dolore ma alipseaa.”</blockquote>
  <div class="name">Joscker Lsore</div><div class="role">VP Engineering</div>
</div>
<div class="abs testi-card" style="left:453px">
  <blockquote>“Lorem ipsum dolor sit amet, ctetulor ehsed do eiusmod tempor incididun ut et dolore ma aliquauilorlore mes ipsusus pendisseiusmod tempor incididunt ut labore et dolore ma alipseaa.”</blockquote>
  <div class="name">Joscker Lsore</div><div class="role">VP Engineering</div>
</div>
<div class="abs testi-card" style="left:771px">
  <blockquote>“Lorem ipsum dolor sit amet, ctetulor ehsed do eiusmod tempor incididun ut et dolore ma aliquauilorlore mes ipsusus pendisseiusmod tempor incididunt ut labore et dolore ma alipseaa.”</blockquote>
  <div class="name">Joscker Lsore</div><div class="role">VP Engineering</div>
</div>
<div class="abs avatar" style="left:246px;background:#e4c9a8" role="img" aria-label="Client portrait"></div>
<div class="abs avatar" style="left:564px;background:#b8a898" role="img" aria-label="Client portrait"></div>
<div class="abs avatar" style="left:882px;background:#c2ad98" role="img" aria-label="Client portrait"></div>

<!-- blog -->
<h2 class="abs display section-title" style="top:2682px">LATEST BLOG POSTS</h2>

<article class="abs blog-card" style="left:150px;width:245px">
  <div class="thumb" role="img" aria-label="Photo of a woman working on a laptop" style="background:linear-gradient(135deg,#3b3a3a,#8a8c90 60%,#d9d6d1)"></div>
  <h3>Lorem ipsum dolor sit amet, consectetur</h3>
  <p>Lorem ipsum dolor sit ametcon sectetur adipiscing elits lordo eiusmod tempor.</p>
  <svg width="32" height="12" viewBox="0 0 32 12" fill="none" stroke="#2f3441" stroke-width="1.5"><path d="M0 6h30M25 1l5 5-5 5"/></svg>
</article>
<article class="abs blog-card" style="left:421px;width:245px">
  <div class="thumb" role="img" aria-label="Photo of colleagues reviewing a screen in a blue-lit office" style="background:linear-gradient(135deg,#1b3a5e,#4f7fa8 55%,#a9c2d8)"></div>
  <h3>Lorem ipsum dolor sit amet, consectetur</h3>
  <p>Lorem ipsum dolor sit ametcon sectetur adipiscing elits lordo eiusmod tempor.</p>
  <svg width="32" height="12" viewBox="0 0 32 12" fill="none" stroke="#2f3441" stroke-width="1.5"><path d="M0 6h30M25 1l5 5-5 5"/></svg>
</article>
<article class="abs blog-card" style="left:689px;width:361px">
  <div class="thumb" role="img" aria-label="Photo of two colleagues in conversation" style="background:linear-gradient(90deg,#2e6b7a,#c9a24a 40%,#c7c1b4 70%,#7d8790)"></div>
  <h3>loremlorem dummyorem ipsum dolor sit amet, consectetur</h3>
  <p>Lorem ipsum dolor sit ametcon sectetur adipiscing elits lordo eiusmod tempor.Risus commodo viverra maecenas accumsan lacus vel facilisis.</p>
  <svg width="32" height="12" viewBox="0 0 32 12" fill="none" stroke="#2f3441" stroke-width="1.5"><path d="M0 6h30M25 1l5 5-5 5"/></svg>
</article>

<!-- partners -->
<div class="abs partners-bg"></div>
<h2 class="abs display section-title partners-title">OUR TRUSTED PARTNERS...</h2>
<div class="abs partner" style="left:180px;width:80px;height:80px;border-radius:50%"></div>
<div class="abs partner" style="left:355px;width:85px;height:80px;border-radius:50%"></div>
<div class="abs partner" style="left:545px;width:64px;height:64px;border-radius:50%;top:3438px"></div>
<div class="abs partner" style="left:712px;width:70px;height:70px;top:3435px"></div>
<div class="abs partner" style="left:862px;width:186px;height:50px;top:3445px"></div>

<!-- footer -->
<div class="abs footer-bg"></div>
<div class="abs footer-brand">
  <div class="brand-square"></div>
  <div class="name">BRACKWELL</div>
  <div class="tag">CONSULTING</div>
</div>
<div class="abs footer-col" style="left:445px">
  <h4>LINKS</h4>
  <ul><li>Services</li><li>Custom Solution Delivery</li><li>Staff Augmentation</li><li>Why Brackwell?</li><li>Brackwell Leadership</li></ul>
</div>
<div class="abs footer-col" style="left:678px">
  <h4>SUPPORT</h4>
  <ul><li>Lorem ipsum dolor</li><li>Rit amet, consectetur</li><li>Adipiscing elit, sed do</li><li>Riusmod temporiunt</li><li>Qlabore et dolmagn</li></ul>
</div>
<div class="abs footer-col" style="left:904px">
  <h4>CONTACT</h4>
  <ul><li>Comming Soon.</li></ul>
</div>
<div class="abs social" aria-label="Social links"><span></span><span></span><span></span><span></span></div>
<div class="abs footer-rule"></div>
<p class="abs copyright">Copyright© 2022 Brackwell Consulting. All Rights Reserved.</p>

</body>
</html>
```